Tarjetas de visita para empresa de aluminio

Empresa con mas de 40 años vendiendo perfiles de aluminio.
Somos fábrica y almacén, queremos renovar la tarjeta de presentación de nuestros comerciales dando una imgen innovadora y tecnógica mezclado con la calidez del respeto al medio ambiente.
Añado el logo de la empresa y actual cara trasera de la tarjeta de visita, el logo es el simbolo WM y la marca TRAVENIC EXTRUSION, la frase 2extrusion y lacado de aluminio" debe cambiarse por "Diseño, extrusión, lacado, anodizado y mecanizado de precisión de aluminio" o en su defecto incluir todos esos servicios que hacemos o una frase mas pegadiza.

We are an aluminium factory, we produce and stock profiles of aluminium.
we want to renew visit card of our sellers, we are looking for something that show innovation, tecnology and environment respect.
Upload our actual logo and back of visit card, logo WM and brand TRAVENIC EXTRUSION must be keept.
Text "Extrusion y lacado de aluminio" must be changed for "Diseño, extrusion, lacado, anodizado y mecanizado de precisión de aluminio" or something like that

```html
<!DOCTYPE html>
<html lang="es">
<head>
<meta charset="utf-8">
<title>Tarjetas de visita – Travenic Extrusion</title>
<link href="https://fonts.googleapis.com/css2?family=Poppins:wght@300;400&family=Comfortaa:wght@400&family=Arimo:wght@400&display=swap" rel="stylesheet">
<style>
  :root {
    --backdrop: #b88a5c;
    --card: #000000;
    --ink: #ededed;
    --ink-soft: #cfcfcf;
    --rule: #8a8a8a;
  }
  * { margin: 0; padding: 0; box-sizing: border-box; }
  html, body { width: 1075px; height: 1200px; overflow: hidden; }
  body { background: var(--backdrop); position: relative; }

  .card {
    position: absolute;
    left: 207px;
    width: 663px;
    height: 395px;
    background: var(--card);
    color: var(--ink);
  }
  .card--front { top: 187px; }
  .card--back { top: 638px; }

  .brand-mark {
    position: absolute;
    border: 3px solid var(--ink);
    border-radius: 50%;
  }
  .brand-name {
    position: absolute;
    font-family: "Poppins", sans-serif;
    font-weight: 300;
    color: var(--ink);
    white-space: nowrap;
    text-align: center;
    transform: translateX(-50%);
  }

  /* front */
  .card--front .brand-mark { left: 120px; top: 96px; width: 88px; height: 88px; }
  .card--front .brand-name { left: 164px; top: 225px; font-size: 21px; letter-spacing: 2px; }
  .website {
    position: absolute; left: 164px; top: 290px; transform: translateX(-50%);
    font-family: "Poppins", sans-serif; font-size: 16px; letter-spacing: 1.5px; color: var(--ink);
  }
  .divider { position: absolute; left: 321px; top: 83px; width: 1px; height: 228px; background: var(--rule); }
  .person { position: absolute; left: 344px; top: 80px; font-family: "Poppins", sans-serif; }
  .person-name { font-size: 19px; letter-spacing: 1.2px; line-height: 24px; }
  .person-role { font-size: 17px; color: var(--ink-soft); letter-spacing: .8px; line-height: 22px; font-weight: 300; }

  .contacts { position: absolute; left: 344px; top: 143px; list-style: none; font-family: "Arimo", sans-serif; font-size: 16px; }
  .contacts li { display: flex; align-items: center; gap: 6px; height: 24.5px; }
  .contacts svg { width: 20px; height: 20px; flex: none; }

  .address { position: absolute; left: 345px; top: 253px; font-family: "Arimo", sans-serif; font-size: 16px; line-height: 22.5px; font-style: normal; color: var(--ink); }

  /* back */
  .card--back .brand-mark { left: 269px; top: 65px; width: 120px; height: 120px; }
  .card--back .brand-name { left: 327px; top: 198px; font-size: 33px; letter-spacing: 3px; }
  .back-rule { position: absolute; left: 115px; top: 286px; width: 425px; height: 1px; background: var(--ink-soft); }
  .tagline {
    position: absolute; left: 327px; top: 297px; transform: translateX(-50%); width: 520px;
    text-align: center; font-family: "Comfortaa", sans-serif; font-size: 18.5px; line-height: 27px; color: var(--ink); letter-spacing: .3px;
  }
</style>
</head>
<body>

<section class="card card--front">
  <span class="brand-mark" aria-hidden="true"></span>
  <p class="brand-name">TRAVENIC EXTRUSION</p>
  <p class="website">www.travenic.com</p>

  <span class="divider"></span>

  <div class="person">
    <p class="person-name">MARCOS ORTEGA LILLO</p>
    <p class="person-role">Comercial</p>
  </div>

  <ul class="contacts">
    <li>
      <svg viewBox="0 0 20 20" fill="none" stroke="#ededed" stroke-width="1.4"><circle cx="10" cy="10" r="9"/><path d="M6.5 5.5l2 2-1 1.5c.8 1.6 2 2.8 3.5 3.5l1.5-1 2 2-1.3 1.3C9.5 14.5 5.5 10.5 5.2 6.8z"/></svg>
      612 48 90 27
    </li>
    <li>
      <svg viewBox="0 0 20 20" fill="none" stroke="#ededed" stroke-width="1.4"><circle cx="10" cy="10" r="9"/><rect x="7" y="4.5" width="6" height="11" rx="1"/><path d="M9.2 13.5h1.6"/></svg>
      954 21 07 63
    </li>
    <li>
      <svg viewBox="0 0 20 20" fill="none" stroke="#ededed" stroke-width="1.4"><circle cx="10" cy="10" r="9"/><rect x="7" y="4.5" width="6" height="3.5"/><rect x="5" y="8" width="10" height="5"/><rect x="7" y="11" width="6" height="4"/></svg>
      954 21 07 64
    </li>
    <li>
      <svg viewBox="0 0 20 20" fill="none" stroke="#ededed" stroke-width="1.4"><circle cx="10" cy="10" r="9"/><rect x="5" y="6.5" width="10" height="7"/><path d="M5 6.5l5 4 5-4"/></svg>
      marcosortega@travenic.com
    </li>
  </ul>

  <address class="address">
    Pol.Ind.Naveral-C/4 N 22<br>
    41930 VILLAVERDE DEL RIO<br>
    (Sevilla), Apartado de Correos 512
  </address>
</section>

<section class="card card--back">
  <span class="brand-mark" aria-hidden="true"></span>
  <p class="brand-name">TRAVENIC EXTRUSION</p>
  <span class="back-rule"></span>
  <p class="tagline">Diseño, extrusion, lacado, anodizado y<br>mecanizado de precisión de aluminio</p>
</section>

</body>
</html>
```